Wordpress Template für Weinkommunikation
Zielgruppe
Kunden und potentielle Kunden, die sich über meine Dienstleistungen und mich informieren wollen.
Meine Arbeitsschwerpunkte sind Kommunikation, PR und Events im Weinbereich.
Meine persönlichen Wein-Schwerpunktländer sind Spanien und Portugal. Die Kunden sind von dort, meine Arbeit ist in Deutschland.
Aufgabenstellung
Ich möchte meine bestehende Website endlich mal richtig gestalten lassen.
- Startseite soll statisch sein.
- Weitere Seiten sollen auch statisch möglich sein.
- 2- oder 3-spaltig
- Template muss Widget-fähig sein
- Möglichkeit der Zweisprachigkeit

```html
<!DOCTYPE html>
<html lang="de">
<head>
<meta charset="utf-8">
<title>Rebe &amp; Rat – Weinkommunikation</title>
<link rel="stylesheet" href="https://fonts.googleapis.com/css2?family=PT+Sans:ital,wght@0,400;0,700;1,400;1,700&family=Arimo:wght@400;700&family=Noto+Sans:wght@400;700&display=swap">
<style>
:root{
  --brown-dark:#4a2410;
  --brown:#6b3a1c;
  --brown-mid:#7a5535;
  --beige:#f6ecd6;
  --beige-light:#fdf8ec;
  --beige-edge:#e3cfa4;
  --cream:#fffdf7;
  --wine-red:#b0100f;
  --text-brown:#4a1c05;
  --orange:#f0a030;
  --gold-line:#c79a55;
  --footer-link:#9a7040;
}
*{box-sizing:border-box;margin:0;padding:0}
html,body{width:1187px;height:1200px;overflow:hidden}
body{background:linear-gradient(90deg,#f0e6d4,#faf5ec 20%,#faf5ec 80%,#efe4cf);font-family:"Arimo",Arial,sans-serif}
.stage{position:absolute;left:0;top:0;width:981px;height:992px;transform:scale(1.21);transform-origin:0 0}
.page{position:absolute;left:42px;top:0;width:900px;height:992px;background:var(--cream)}
.abs{position:absolute}
/* header */
.header{left:0;top:0;width:900px;height:97px;background:#fff}
.brand{left:24px;top:14px;display:flex;align-items:center;gap:10px}
.brand-mark{width:60px;height:60px;background:var(--wine-red)}
.brand-name{font-family:"PT Sans",sans-serif;font-weight:700;font-size:22px;line-height:24px;color:var(--brown-dark)}
.social{left:559px;top:59px;display:flex;gap:5px}
.social span{width:24px;height:24px;border-radius:3px;background:var(--beige-edge)}
/* nav */
.nav{left:0;top:97px;width:900px;height:35px;background:linear-gradient(180deg,#6e3d1f,#4a2410)}
.nav ul{list-style:none;display:flex;position:absolute;left:17px;top:9px;font-family:"PT Sans",sans-serif;font-size:13px;color:#fff}
.nav li{padding:0 8px;border-left:1px solid var(--orange);line-height:14px}
.nav li:first-child{border-left:0}
.search{position:absolute;left:786px;top:6px;width:88px;height:20px;background:#f6e7c2;border:1px solid #c7a56b;font-size:11px;color:var(--brown-dark);padding:3px 4px}
.search-go{position:absolute;left:879px;top:10px;font-size:11px;color:#f6e7c2;font-family:"PT Sans",sans-serif}
/* hero */
.hero{left:0;top:132px;width:900px;height:168px;background:linear-gradient(90deg,#3a2012 0%,#8a5a3a 30%,#5a2a15 55%,#a0703d 80%,#d4b68a 100%)}
.hero-title{left:254px;top:96px;font-family:"PT Sans",sans-serif;font-weight:700;font-style:italic;font-size:17px;color:#fff}
.hero-sub{left:268px;top:121px;font-family:"PT Sans",sans-serif;font-style:italic;font-size:16px;color:var(--orange)}
/* main */
.welcome{left:51px;top:341px;font-family:"PT Sans",sans-serif;font-weight:700;font-style:italic;font-size:15px;color:var(--wine-red)}
.portrait{left:49px;top:375px;width:106px;height:125px;border:1px solid var(--beige-edge);background:linear-gradient(180deg,#d8dfe4,#3c3c44)}
.lead{left:185px;top:375px;width:330px;font-family:"Noto Sans",Verdana,sans-serif;font-weight:700;font-size:10.6px;line-height:13.6px;color:var(--text-brown);letter-spacing:.1px}
.body-text{left:48px;top:516px;width:470px;font-size:10.6px;line-height:13px;color:var(--text-brown)}
.body-text p{margin-bottom:13px}
.body-text .call{color:var(--wine-red)}
.signature{left:48px;top:652px;width:180px;height:48px;background:linear-gradient(90deg,#fff,#f6f0e6)}
.sign-name{left:48px;top:701px;font-size:10.6px;color:var(--wine-red)}
.divider{left:48px;top:735px;width:478px;height:1px;background:linear-gradient(90deg,transparent,var(--gold-line),transparent)}
.news-photo{left:49px;top:758px;width:122px;height:97px;border:1px solid var(--beige-edge);background:linear-gradient(180deg,#fafafa,#d0d0d0)}
.news-title{left:186px;top:758px;font-family:"Noto Sans",Verdana,sans-serif;font-size:11px;color:var(--text-brown)}
.news-title b{font-weight:700}
.news-list{left:188px;top:784px;list-style:none;font-size:10.6px;line-height:13.1px;color:#000}
.news-list li{padding-left:16px;position:relative}
.news-list li::before{content:"";position:absolute;left:0;top:3px;width:6px;height:6px;background:#b59a6a}
/* sidebar */
.sidebar{left:557px;top:207px;width:318px;height:688px;background:linear-gradient(180deg,#f3e4c2,#e6d3a9);border:1px solid #d8c090;box-shadow:0 2px 6px rgba(90,60,20,.3)}
.tabs{left:22px;top:12px;display:flex;gap:2px}
.tabs span{width:29px;height:23px;background:#d8c49a;color:#fff;font-family:"PT Sans",sans-serif;font-size:15px;text-align:center;line-height:23px}
.tabs span.active{background:#c8ae7a;height:26px;margin-top:-3px}
.box{background:var(--beige-light);border:1px solid var(--beige-edge)}
.blog-box{left:11px;top:35px;width:296px;height:244px}
.blog-head{left:16px;top:17px;font-family:"Noto Sans",Verdana,sans-serif;font-weight:700;font-size:10.6px;line-height:14px;color:var(--text-brown)}
.rss{left:238px;top:10px;width:48px;height:48px;border-radius:8px;background:#f07a20}
.blog-post{left:16px;top:56px;font-family:"Noto Sans",Verdana,sans-serif;font-weight:700;font-size:10.8px;color:var(--text-brown)}
.blog-teaser{left:16px;top:82px;width:240px;font-size:10.2px;line-height:13.2px;color:var(--text-brown)}
.blog-photos{left:12px;top:155px;width:170px;height:52px;background:linear-gradient(90deg,#7a8a55,#a9b88a,#8c7a5a)}
.blog-more{left:219px;top:220px;font-family:"Noto Sans",Verdana,sans-serif;font-weight:700;font-size:10.4px;color:var(--wine-red)}
.video-box{left:11px;top:300px;width:296px;height:220px}
.player{left:8px;top:12px;width:278px;height:199px;border-radius:8px;background:linear-gradient(180deg,#8c6a45,#6e4e30);border:1px solid #5a3c22}
.video{left:11px;top:13px;width:256px;height:118px;background:linear-gradient(90deg,#4a5540,#8aa070 60%,#c8d0b0)}
.video-cap{left:12px;top:112px;font-family:"PT Sans",sans-serif;font-weight:700;font-size:12px;color:#fff}
.track{left:20px;top:139px;width:238px;height:6px;border-radius:3px;background:#3a2414}
.knob{left:28px;top:136px;width:12px;height:12px;border-radius:50%;background:#d8b88a}
.controls{left:58px;top:154px}
.newsletter{left:11px;top:536px;width:296px;height:129px}
.nl-title{left:9px;top:9px;font-family:"Noto Sans",Verdana,sans-serif;font-weight:700;font-size:10.8px;color:var(--text-brown)}
.nl-img{left:8px;top:30px;width:54px;height:74px;border:1px solid var(--beige-edge);background:linear-gradient(180deg,#2a2a2a,#6a5a40)}
.nl-text{left:72px;top:29px;width:200px;font-size:10.6px;line-height:13px;color:var(--text-brown)}
.nl-input{left:76px;top:82px;width:117px;height:20px;background:#f0e4c8;border:1px solid #d8c090}
.nl-submit{left:208px;top:105px;font-family:"Noto Sans",Verdana,sans-serif;font-weight:700;font-size:10.4px;color:var(--wine-red)}
/* footer */
.footer-glow{left:90px;top:905px;width:740px;height:30px;background:radial-gradient(ellipse at center,#f6e2b4,transparent 70%)}
.footer-links{left:57px;top:940px;font-family:"PT Sans",sans-serif;font-size:11px;color:var(--footer-link)}
.footer-partner{left:770px;top:929px;font-family:"PT Sans",sans-serif;font-weight:700;font-size:15px;color:var(--wine-red)}
.footer-band{left:0;top:966px;width:900px;height:26px;background:linear-gradient(180deg,#3a1a08,#5a2c12)}
</style>
</head>
<body>
<div class="stage">
 <div class="page">
  <header class="header abs">
   <div class="brand abs"><span class="brand-mark"></span><span class="brand-name">Rebe &amp; Rat<br>Jonas K. Berland</span></div>
   <div class="social abs"><span></span><span></span><span></span><span></span><span></span><span></span><span></span><span></span><span></span><span></span><span></span></div>
  </header>
  <nav class="nav abs">
   <ul><li>Home</li><li>Wer</li><li>Referenzen</li><li>Buchtipps</li><li>Wein-News</li><li>Wein-Glossar</li><li>Links</li><li>Kontakt</li><li>Blog</li></ul>
   <div class="search">Suche</div><span class="search-go">go</span>
  </nav>
  <section class="hero abs" role="img" aria-label="Weinexperte beim Verkosten eines Rotweins vor einem Regal mit Weinflaschen">
   <div class="hero-title abs">Weinkommunikation</div>
   <div class="hero-sub abs">Full Service Beratung vom Wein-Profi</div>
  </section>

  <h1 class="welcome abs">Willkommen bei Rebe &amp; Rat</h1>
  <div class="portrait abs" role="img" aria-label="Porträt des Weinberaters"></div>
  <p class="lead abs">Mit Rebe &amp; Rat möchte ich Ihnen vor allem mein Wissen über Wein - insbesondere der Iberischen Halbinsel - über die Weinbau-Länder, die unterschiedlichen Regionen, die abwechslungsreichen Landschaften, die unzähligen Kellereien, die Winzerpersönlichkeiten, aber auch meine ganz persönlichen Eindrücke und Erlebnisse zur Kultur, zur Gastronomie, zu den Menschen und zum Leben in Spanien, Portugal, der Weinwelt und zum Thema Genuss allgemein zugänglich machen.</p>
  <div class="body-text abs">
   <p>&nbsp;Durch die langjährige Erfahrung im internationalen Weingrosshandel und der Weinszene sind die Bereiche Kommunikation, PR und Marketing, sowie die Sortiments- und Einkaufsberatung, neben den Schulungen ein wichtiger Bestandteil des Angebotes.</p>
   <p>In Partnerschaft mit einer Vielzahl von Sommeliers, Weinprofis und anderen Freiberuflern können wir Ihnen darüber hinaus ein breites Spektrum an Leistungen rund um das Thema Wein und Genuss anbieten. Das garantiert Ihnen massgeschneiderte Weinkompetenz ganz nach Ihrem Geschmack und Ihren Wünschen!</p>
   <p class="call">Sprechen Sie uns einfach an. Wir sind für Sie da!</p>
  </div>
  <div class="signature abs" role="img" aria-label="Handschriftliche Unterschrift"></div>
  <div class="sign-name abs">Ihr Jonas K. Berland</div>
  <div class="divider abs"></div>
  <div class="news-photo abs" role="img" aria-label="Weingläser mit Rotwein"></div>
  <div class="news-title abs"><b>Aktuelle Wein-News</b> &nbsp;(by Vinoportal.de)</div>
  <ul class="news-list abs">
   <li>Winzer relativ zufrieden</li><li>Erste-Lage-Spätlesen im Rampenlicht</li><li>Neue Sommelier-Ausbildung</li><li>Ernte 2010 in Südtirol: Wenig, aber sehr gut</li><li>Betrüger verurteilt</li><li>Majestät kommt von der Ahr</li><li>Weinköniginnen-Halbfinale beendet</li><li>Neue Deutsche Weinkönigin steht vor der Wahl</li>
  </ul>

  <aside class="sidebar abs">
   <div class="tabs abs"><span>1</span><span>2</span><span>3</span><span class="active">4</span><span>5</span><span>6</span></div>
   <div class="blog-box box abs">
    <div class="blog-head abs">blog.rebe-rat.de<br>mein Blog mit Infos, News und mehr.</div>
    <div class="rss abs"><svg width="48" height="48" viewBox="0 0 48 48"><circle cx="14" cy="34" r="4" fill="#fff"/><path d="M10 22a16 16 0 0 1 16 16M10 12a26 26 0 0 1 26 26" stroke="#fff" stroke-width="5" fill="none"/></svg></div>
    <div class="blog-post abs">Eine Woche in Brasilien</div>
    <p class="blog-teaser abs">Auf Einladung von "Vinhos do Sul" habe ich mir eine Woche lang den Weinbau im Süden von Brasilien angesehen. Eine ganz neue Erfahrung für mich...</p>
    <div class="blog-photos abs" role="img" aria-label="Fotos von Weinbergen in Südbrasilien"></div>
    <div class="blog-more abs">zum Blog</div>
   </div>
   <div class="video-box box abs">
    <div class="player abs">
     <div class="video abs" role="img" aria-label="Videostandbild einer Autofahrt durch Weinberge">
      <div class="video-cap abs">DIE FACETTEN DER REBSORTE GRANACHA</div>
     </div>
     <div class="track abs"></div><div class="knob abs"></div>
     <svg class="controls abs" width="160" height="44" viewBox="0 0 160 44">
      <g fill="#d8b88a"><circle cx="12" cy="22" r="9"/><circle cx="42" cy="22" r="13"/><circle cx="82" cy="22" r="19"/><circle cx="122" cy="22" r="13"/><circle cx="152" cy="22" r="9"/></g>
      <g fill="#6e4e30"><path d="M7 22l5-4v8zM12 22l5-4v8z"/><rect x="36" y="16" width="12" height="12"/><path d="M76 12l14 10-14 10z"/><rect x="116" y="15" width="4" height="14"/><rect x="124" y="15" width="4" height="14"/><path d="M147 18l5 4-5 4zM152 18l5 4-5 4z"/></g>
     </svg>
    </div>
   </div>
   <div class="newsletter box abs">
    <div class="nl-title abs">Newsletter</div>
    <div class="nl-img abs" role="img" aria-label="Weinflasche mit Etikett"></div>
    <p class="nl-text abs"><b>Melden Sie sich an</b> und bleiben immer aktuell informiert über Interessantes aud der Weinwelt</p>
    <div class="nl-input abs"></div>
    <div class="nl-submit abs">Jetzt anmelden</div>
   </div>
  </aside>

  <div class="footer-glow abs"></div>
  <div class="footer-links abs">Kontakt | Impressum | Blog | Wein-Glossar | Adresse</div>
  <div class="footer-partner abs">Vinoportal.de</div>
  <div class="footer-band abs"></div>
 </div>
</div>
</body>
</html>
```